An expert for Professional and Technical Evaluation of Painting Work Needs a New Letterhead Design

I own a mid-sized painting company and also work as an expert for professional and technical evaluation of painting work in the area of Zurich.

Please read the project description and the must-have-requirements carefully!

I attached 1 PDF which will help you create a new letterhead design:

THE NEW DESIGN DOESN'T NEED A LOGO! (Because it won't represent a company, it represents only a service)
Updates

Dear designers We had a discussion about the location/placement of the design and came to the conclusion that we only want the design to be in the header area of the A4-paper. We would be glad to receive some revised version of your designs. Thank you and kind regards!

Project Deadline Extended
Reason: Due to the fact that only 20% of the designer have understood the brief and submitted designs that have met the requirements we decided to extend the contest deadline.

Project Deadline Extended
Reason: A great deal of good designs were submitted in the last few days. A big thank you to all the participating designers for your good work. We need a few more days to discuss some changes with certain designers and to decide which design will win.

Target Market(s)

(Insurance) Companies, partly also private clients.

Industry/Entity Type

Painting

Colors

Designer to choose colors to be used in the design.

Requirements
Must have
• All information (text, phone numbers, ...) of the old design ("old_letterhead_design.pdf") has also to be in the new one. Additional to that there are a few changes:
The phone numbers "01 583 61 47" and "01 583 61 37" change to "044 583 61 47" and "044 583 61 37". And please mention also this email address: gutachten@valmorkeller.example .

- The design should only be in the header-area of the A4-paper. An the background color of the A4-paper will be white.

- The design should consist of two designs. One for the first page and a smaller version of the design for the following pages.

- THE NEW DESIGN DOESN'T NEED A LOGO! You can make a design with geometric forms, ...

- The new design should have a juridical look. It should only contain colors like brown, fawn, black, light green, ...... colors which look serious/reliable.
Nice to have
• Geometric Forms, Symbols or other design elements.

- It would also be nice to have some design elements which emphasize the kind of work we are offering.

```html
<!DOCTYPE html>
<html lang="de">
<head>
<meta charset="utf-8">
<title>Valmor Keller – Briefkopf</title>
<link rel="stylesheet" href="https://fonts.googleapis.com/css2?family=Ubuntu:wght@400;500;700&display=swap">
<style>
  :root {
    --paper: #ffffff;
    --name-brown: #6b5a4f;
    --fawn: #a98b6c;
    --rule: #c9bfb5;
    --ink: #2a2a2a;
    --ink-soft: #555555;
  }
  * { margin: 0; padding: 0; box-sizing: border-box; }
  html, body {
    width: 1200px; height: 1000px; overflow: hidden;
    background: var(--paper);
  }
  .letter { position: relative; width: 1200px; height: 1000px; }

  .letterhead { position: absolute; left: 367px; top: 100px; width: 386px; }
  .letterhead__name {
    font-family: "Ubuntu", sans-serif; font-weight: 400;
    font-size: 30px; line-height: 34px; color: var(--name-brown);
    letter-spacing: 1px; white-space: nowrap;
  }
  .letterhead__services {
    font-family: "Ubuntu", sans-serif; font-weight: 400;
    font-size: 10.5px; line-height: 14px; color: var(--fawn);
    letter-spacing: 0.4px; margin-top: 4px; white-space: nowrap;
  }
  .letterhead__rule { width: 280px; height: 1px; background: var(--rule); margin-top: 7px; }
  .letterhead__contact {
    font-family: "Ubuntu", sans-serif; font-size: 8px; line-height: 11px;
    color: var(--ink-soft); margin-top: 6px; white-space: nowrap;
  }
  .letterhead__contact b { font-weight: 500; color: var(--ink); }

  .letter__subject {
    position: absolute; left: 367px; top: 266px;
    font-family: "Ubuntu", sans-serif; font-weight: 500;
    font-size: 12.5px; color: var(--ink);
  }
  .letter__body {
    position: absolute; left: 367px; top: 292px; width: 386px;
    font-family: "Ubuntu", sans-serif; font-size: 12.8px; line-height: 15px;
    color: var(--ink); text-align: justify; hyphens: auto;
  }
  .letter__body p { margin-bottom: 15px; }
  .letter__body p.tight { margin-bottom: 0; text-align: left; }

  .letter__meta {
    position: absolute; left: 771px; top: 292px;
    font-family: "Ubuntu", sans-serif; font-size: 12.5px; line-height: 15px;
    color: var(--ink);
  }
  .letter__meta dt { font-weight: 500; }
  .letter__meta dd { margin-bottom: 37px; }

  .signature { position: absolute; left: 396px; top: 782px; }
  .signature__mark { display: block; width: 92px; height: 24px; }
  .signature__name {
    font-family: "Ubuntu", sans-serif; font-weight: 500;
    font-size: 8px; color: var(--ink); margin: 4px 0 0 4px;
  }
</style>
</head>
<body>
<main class="letter">
  <header class="letterhead">
    <h1 class="letterhead__name">Valmor Keller</h1>
    <p class="letterhead__services">Gutachten · Expertisen · Devisierungen · Farbberatungen · Dekorative Gestaltungen</p>
    <div class="letterhead__rule"></div>
    <p class="letterhead__contact">eidg. dipl. Malermeister / Lindenweg 12, 8800 Thalwil<br>
      <b>Telefon</b> 044 583 61 47 / <b>Fax</b> 044 583 61 37 / <b>Natel</b> 079 412 30 56</p>
  </header>

  <h2 class="letter__subject">Lorem ipsum dolor sit amet, ei eros vidit sonet eum</h2>

  <section class="letter__body">
    <p>Lorem ipsum dolor sit amet, ei eros vidit sonet eum, sed ea aliquam offendit. Reque quando labitur nec in, no solum ceteros est. Accumsan pertinacia an qui. Te vidisse recteque pro, cu per habemus officiis, eos ex malis posidonium omittantur. Appetere principes eloquentiam vis ei, an mea alia petentium dignissim, te justo omnium duo.</p>
    <p>Movet laoreet delicatissimi cum id. Essent dissentiet cu cum, atqui augue iriure qui ea. Liber propriae ei sed. Euismod ornatus scaevola et pro.</p>
    <p>Verterem interesset disputationi vim et, laudem persecuti quo eu. Mea viderer vulputate ut. Ad scripta scaevola appetere usu, omnium forensibus sed cu, dolorum admodum postulant mea ei. Eos ut ubique graeco insolens, etiam electram assentior cum at.</p>
    <p>In eos solum verterem facilisis, magna scaevola explicari has ex, at vidisse percipitur cum. At dicam postea luptatum sea, sed te timeam principes disputando, postea scaevola eloquentiam quo eu. Cetero concludaturque cu ius, nam erat detraxit ut, in his cetero vocent erroribus. Eu sint nulla comprehensam qui. Dolor dolorum splendide ei est, id usu inani liber deterruisset.</p>
    <p class="tight">Omnis intellegat intellegam duo cu, no ornatus partiendo referrentur has</p>
    <p>Verterem interesset disputationi vim et, laudem persecuti quo eu. Mea viderer vulputate ut. Ad scripta scaevola appetere usu, omnium forensibus sed cu, dolorum admodum postulant mea ei. Eos ut ubique graeco insolens, etiam electram assentior cum at.</p>
  </section>

  <dl class="letter__meta">
    <dt>Date</dt><dd>Sept. 25, 2014</dd>
    <dt>From</dt><dd>Mr. Valmor Keller<br>CEO</dd>
    <dt>To</dt><dd>Mr. Dario Venn<br>CEO Business</dd>
  </dl>

  <footer class="signature">
    <svg class="signature__mark" role="img" aria-label="Handwritten signature" viewBox="0 0 92 24">
      <rect x="0" y="6" width="92" height="12" rx="6" fill="#e6e6e6"/>
    </svg>
    <p class="signature__name">Your Name</p>
  </footer>
</main>
</body>
</html>
```